Business Cards

Need a neat design for a new business card

Industry/Entity Type

Residential Construction

Contact Information for Business Card

Company Name- KOVE Construction Inc.
Owner- Marcus Tolliver
Phone number- (555)203-7481
Email- kovecohomes@brindlemail.example
Facebook- www.socialpage.example/kovecohomes

Colors
fefdec

```html
<!DOCTYPE html>
<html lang="en">
<head>
<meta charset="utf-8">
<title>KOVE Construction Inc. — Business Card</title>
<link href="https://fonts.googleapis.com/css2?family=Lato:wght@400;700;900&display=swap" rel="stylesheet">
<style>
  :root {
    --backdrop: #d6d6d6;
    --card-light: #ffffff;
    --card-dark: #07080a;
    --ink: #0a0a0a;
    --muted: #6d6d6d;
    --reverse: #ffffff;
  }
  * { box-sizing: border-box; margin: 0; padding: 0; }
  html, body {
    width: 1200px;
    height: 1143px;
    overflow: hidden;
    background: var(--backdrop);
    font-family: "Lato", Arial, sans-serif;
  }
  .card {
    position: absolute;
    left: 299px;
    width: 602px;
    height: 343px;
  }
  .card--front { top: 180px; background: var(--card-light); }
  .card--back  { top: 621px; background: var(--card-dark); }

  .accent-bar {
    position: absolute;
    left: 0; top: 172px;
    width: 12px; height: 45px;
    background: var(--ink);
  }
  .person {
    position: absolute;
    left: 35px; top: 170px;
  }
  .person__name {
    font-weight: 900;
    font-size: 28px;
    line-height: 1;
    color: var(--ink);
    letter-spacing: -0.2px;
  }
  .person__role {
    margin-top: 6px;
    font-size: 16px;
    color: var(--muted);
  }
  .contacts {
    position: absolute;
    left: 32px; top: 249px;
    list-style: none;
  }
  .contacts li {
    display: flex;
    align-items: center;
    height: 23px;
    font-size: 16px;
    color: var(--muted);
  }
  .contacts svg {
    width: 18px; height: 18px;
    margin-right: 11px;
    flex: none;
  }

  .brand {
    position: absolute;
    display: flex;
    flex-direction: column;
    align-items: center;
    font-weight: 700;
  }
  .brand__mark {
    width: 14px; height: 14px;
    margin-bottom: 10px;
  }
  .brand__name { line-height: 1; }
  .brand__sub { letter-spacing: 2px; margin-top: 8px; line-height: 1; }

  .card--front .brand { left: 398px; top: 50px; width: 172px; color: var(--ink); }
  .card--front .brand__mark { background: var(--ink); }
  .card--front .brand__name { font-size: 56px; }
  .card--front .brand__sub { font-size: 13px; }

  .card--back .brand { left: 0; right: 0; top: 92px; color: var(--reverse); }
  .card--back .brand__mark { background: var(--reverse); width: 18px; height: 18px; margin-bottom: 14px; }
  .card--back .brand__name { font-size: 84px; }
  .card--back .brand__sub { font-size: 16px; letter-spacing: 3px; margin-top: 12px; }
</style>
</head>
<body>
  <section class="card card--front">
    <div class="brand">
      <span class="brand__mark"></span>
      <span class="brand__name">KOVE</span>
      <span class="brand__sub">CONSTRUCTION</span>
    </div>

    <span class="accent-bar"></span>
    <div class="person">
      <h1 class="person__name">Marcus Tolliver</h1>
      <p class="person__role">Owner</p>
    </div>

    <ul class="contacts">
      <li>
        <svg viewBox="0 0 24 24" aria-hidden="true"><path fill="#0a0a0a" d="M6.6 10.8c1.4 2.8 3.8 5.1 6.6 6.6l2.2-2.2c.3-.3.7-.4 1-.2 1.1.4 2.3.6 3.6.6.6 0 1 .4 1 1V20c0 .6-.4 1-1 1C10.6 21 3 13.4 3 4c0-.6.4-1 1-1h3.5c.6 0 1 .4 1 1 0 1.3.2 2.5.6 3.6.1.3 0 .7-.2 1z"/></svg>
        (555)203-7481
      </li>
      <li>
        <svg viewBox="0 0 24 24" aria-hidden="true"><rect x="2" y="5" width="20" height="14" fill="#0a0a0a"/><path d="M2.5 5.5 12 13l9.5-7.5M2.5 18.5 9.5 11.5M21.5 18.5l-7-7" stroke="#fff" stroke-width="1.4" fill="none"/></svg>
        kovecohomes@brindlemail.example
      </li>
      <li>
        <svg viewBox="0 0 24 24" aria-hidden="true"><circle cx="12" cy="12" r="9.5" fill="none" stroke="#0a0a0a" stroke-width="2"/></svg>
        kovecohomes
      </li>
    </ul>
  </section>

  <section class="card card--back">
    <div class="brand">
      <span class="brand__mark"></span>
      <span class="brand__name">KOVE</span>
      <span class="brand__sub">CONSTRUCTION</span>
    </div>
  </section>
</body>
</html>
```